Velisto Events Business Card

We need a business cards that stands out to our clients. We are company who targets prestige clients to spend money with us on experiences, so our image needs to be prestige
Target Market(s)
Corporate
Contact Information for Business Card
There will be four different names on the business cards
Dana Morrowby
Director
O: 02 5147 3086
M: 0451 692 038
E: info@velistoevents.example.au
Facebook: @velistoevents
Instagram: velistoevents
www.velistoevents.example.au
Nathaniel Morrowby
Director
O: 02 5147 3086
M: 0467 215 904
Facebook: @velistoevents
Instagram: velistoevents
www.velistoevents.example.au
Teodor Vinkel
Director
O: 02 5147 3086
M: 0478 903 527
Facebook: @velistoevents
Instagram: velistoevents
www.velistoevents.example.au
Mabel Hartung
Director
O: 02 5147 3086
Facebook: @velistoevents
Instagram: velistoevents
www.velistoevents.example.au
Colors
Designer to choose colors to be used in the design.
Look and feel

```html
<!DOCTYPE html>
<html lang="en">
<head>
<meta charset="utf-8">
<title>Velisto Events Business Card</title>
<link href="https://fonts.googleapis.com/css2?family=Source+Sans+3:wght@400;600;700&display=swap" rel="stylesheet">
<style>
  :root {
    --stage: #1a1a1c;
    --card: #27224f;
    --card-edge: #201c45;
    --gold: #d9ae3c;
    --text-light: #d8d6e6;
    --text-muted: #b9b6cf;
  }
  * { margin: 0; padding: 0; box-sizing: border-box; }
  html, body {
    width: 1200px; height: 900px; overflow: hidden;
    background: var(--stage);
    font-family: "Source Sans 3", "Myriad Pro", Arial, sans-serif;
  }
  .canvas { position: relative; width: 1200px; height: 900px; }
  .card {
    position: absolute; left: 320px; width: 560px; height: 320px;
    background: var(--card);
    border-radius: 26px;
    box-shadow: 0 18px 40px rgba(0,0,0,.55);
    overflow: hidden;
  }
  .card--back { top: 90px; }
  .card--front { top: 490px; }

  .brand-name {
    font-weight: 600;
    color: var(--gold);
    text-transform: uppercase;
    letter-spacing: .28em;
    white-space: nowrap;
  }
  .card--back .brand-name {
    position: absolute; left: 0; right: 0; top: 130px;
    text-align: center; font-size: 34px;
  }
  .website {
    position: absolute; right: 38px; bottom: 34px;
    color: var(--text-light); font-size: 15px;
  }

  .card--front .brand-name {
    position: absolute; right: 36px; top: 110px;
    font-size: 26px; text-align: right;
  }
  .address {
    position: absolute; right: 36px; top: 182px;
    text-align: right; color: var(--text-light);
    font-size: 16px; line-height: 1.35;
  }
  .contact {
    position: absolute; left: 40px; top: 166px;
  }
  .contact__name {
    color: var(--gold); font-weight: 700; font-size: 22px;
    text-transform: uppercase; letter-spacing: .01em;
  }
  .contact__role {
    color: var(--text-muted); font-size: 16px; margin-bottom: 12px;
  }
  .contact__list { list-style: none; }
  .contact__list li {
    display: flex; align-items: center; gap: 8px;
    color: var(--text-light); font-size: 16px; line-height: 1.45;
  }
  .contact__list svg { width: 13px; height: 13px; fill: var(--gold); flex: none; }
</style>
</head>
<body>
<main class="canvas">

  <section class="card card--back" aria-label="Card back">
    <p class="brand-name">Velisto Events</p>
    <p class="website">www.velistoevents.example.au</p>
  </section>

  <section class="card card--front" aria-label="Card front">
    <p class="brand-name">Velisto Events</p>
    <p class="address">12345, Address Goes Here<br>Country Name, 123456</p>

    <div class="contact">
      <p class="contact__name">Dana Morrowby</p>
      <p class="contact__role">Managing Director</p>
      <ul class="contact__list">
        <li>
          <svg viewBox="0 0 16 16" aria-hidden="true"><path d="M1 5c0-2 3-3 7-3s7 1 7 3v1h-4V5H5v1H1z M3 7h10l1 7H2z M8 9a2 2 0 1 0 0 4a2 2 0 1 0 0-4z"/></svg>
          02 5147 3086
        </li>
        <li>
          <svg viewBox="0 0 16 16" aria-hidden="true"><path d="M4 0h8a1 1 0 0 1 1 1v14a1 1 0 0 1-1 1H4a1 1 0 0 1-1-1V1a1 1 0 0 1 1-1zm1 2v10h6V2zm3 11a1 1 0 1 0 0 2a1 1 0 1 0 0-2z"/></svg>
          0451 692 038
        </li>
        <li>
          <svg viewBox="0 0 16 16" aria-hidden="true"><path d="M0 3h16v1L8 9 0 4zm0 3l8 5 8-5v7H0z"/></svg>
          info@velistoevents.example.au
        </li>
      </ul>
    </div>
  </section>

</main>
</body>
</html>
```